Catalogue Design Project

we are a catering company but we also do room decor for our events. i am trying to make an easy catalogue of our decor products for clients to select and budget for their theming. We are also considering sub hiring our decor to outside clients and vendors.
I have been putting together a outline on publisher but I am not a designer and it lacks that artistic touch and polish. I would like the finished product in INDD, PDF and if at all possible publisher.
Updates
Target Market(s)
corporate events
Industry/Entity Type
Catering
Requirements
Must have
- the catalog must be at least 30 pages and use as many photos as possible I have provided - I have more photos if required. I have uploaded the publisher file I have created to http://www.filecrate-example.net/file/7kt4mw as well as a pdf http://www.filecrate-example.net/file/3rb9xq
MUST HAVE the grey banner with the colors.
Nice to have
- Would be nice to have final in publisher as well as INDD and a pfd.
Should not have
- should not look cheap or too difficult to read.

```html
<!DOCTYPE html>
<html lang="en">
<head>
<meta charset="utf-8">
<title>Table Runners – Decor Catalogue</title>
<link rel="stylesheet" href="https://fonts.googleapis.com/css2?family=Montserrat:wght@300;400;500&display=swap">
<style>
  :root {
    --paper: #ffffff;
    --ink: #2b2b2b;
    --accent: #1f9cc6;
    --leader: #8a8a8a;
    --footer-ink: #ffffff;
    --blush: #c4a195;
    --gold: #a98650;
    --flock-ground: #e9e3e4;
    --flock-red: #b8283a;
    --burgundy: #731c2c;
    --burgundy-light: #8c3542;
    --ivory: #e8ddd2;
    --rose-ground: #cfaaa0;
    --damask-grey: #6f7b7a;
    --teal: #117a82;
    --teal-deep: #0c666d;
    --blossom: #cfe0df;
  }
  * { margin: 0; padding: 0; box-sizing: border-box; }
  html, body {
    width: 1200px; height: 463px; overflow: hidden;
    background: var(--paper);
  }
  .spread {
    position: relative; width: 1200px; height: 463px;
    background: var(--paper);
    font-family: "Montserrat", Arial, sans-serif;
    color: var(--ink);
  }

  /* Fabric photo placeholders */
  .fabric-photo { position: absolute; top: 0; height: 463px; }
  .fabric-photo--blush-gold {
    left: 0; width: 150px;
    background:
      radial-gradient(ellipse 60% 30% at 30% 20%, rgba(169,134,80,0.55), transparent 70%),
      radial-gradient(ellipse 50% 25% at 75% 55%, rgba(169,134,80,0.45), transparent 70%),
      radial-gradient(ellipse 60% 30% at 25% 90%, rgba(169,134,80,0.6), transparent 70%),
      var(--blush);
  }
  .fabric-photo--red-flock {
    left: 155px; width: 163px;
    background:
      radial-gradient(ellipse 70% 22% at 60% 12%, rgba(184,40,58,0.85), transparent 72%),
      radial-gradient(ellipse 55% 20% at 30% 42%, rgba(184,40,58,0.8), transparent 72%),
      radial-gradient(ellipse 65% 20% at 70% 68%, rgba(184,40,58,0.8), transparent 72%),
      radial-gradient(ellipse 70% 18% at 40% 95%, rgba(184,40,58,0.85), transparent 72%),
      var(--flock-ground);
  }
  .fabric-photo--burgundy-vine {
    left: 323px; width: 163px;
    background:
      radial-gradient(ellipse 40% 14% at 35% 22%, rgba(232,221,210,0.35), transparent 75%),
      radial-gradient(ellipse 40% 14% at 65% 52%, rgba(232,221,210,0.35), transparent 75%),
      radial-gradient(ellipse 40% 14% at 35% 82%, rgba(232,221,210,0.35), transparent 75%),
      linear-gradient(170deg, var(--burgundy) 0%, var(--burgundy-light) 50%, var(--burgundy) 100%);
  }
  .fabric-photo--rose-damask {
    left: 492px; width: 162px;
    background:
      radial-gradient(ellipse 70% 20% at 50% 18%, rgba(111,123,122,0.8), transparent 72%),
      radial-gradient(ellipse 60% 18% at 45% 50%, rgba(111,123,122,0.7), transparent 72%),
      radial-gradient(ellipse 70% 20% at 55% 82%, rgba(111,123,122,0.8), transparent 72%),
      var(--rose-ground);
  }
  .fabric-photo--teal-blossom {
    left: 660px; width: 264px;
    background:
      radial-gradient(ellipse 35% 40% at 85% 40%, rgba(207,224,223,0.45), transparent 72%),
      radial-gradient(ellipse 25% 18% at 15% 75%, rgba(207,224,223,0.35), transparent 72%),
      linear-gradient(150deg, var(--teal-deep) 0%, var(--teal) 55%, var(--teal-deep) 100%);
  }

  .folio-left {
    position: absolute; left: 19px; top: 430px;
    font-size: 9.5px; font-weight: 400; letter-spacing: 0.3px;
    color: var(--footer-ink);
    white-space: nowrap;
  }
  .price-panel {
    position: absolute; left: 968px; top: 0; width: 192px;
  }
  .price-panel__title {
    position: absolute; left: 0; right: 0; top: 30px;
    text-align: center;
    font-size: 20px; font-weight: 400; letter-spacing: 1.2px;
    color: var(--accent);
  }
  .price-list { list-style: none; position: absolute; top: 68px; left: 0; width: 192px; }
  .price-list__item {
    display: flex; align-items: baseline;
    height: 19.7px; font-size: 8.6px; font-weight: 400;
    white-space: nowrap;
  }
  .price-list__leader {
    flex: 1; margin: 0 1px;
    border-bottom: 1px dotted var(--leader);
    transform: translateY(-2px);
  }
  .folio-right {
    position: absolute; left: 1168px; top: 434px;
    font-size: 9.5px; color: var(--ink);
  }
</style>
</head>
<body>
<div class="spread">
  <div class="fabric-photo fabric-photo--blush-gold" role="img" aria-label="Close-up photo of blush fabric with gold floral embroidery"></div>
  <div class="fabric-photo fabric-photo--red-flock" role="img" aria-label="Close-up photo of white fabric with red flocked damask pattern"></div>
  <div class="fabric-photo fabric-photo--burgundy-vine" role="img" aria-label="Close-up photo of burgundy fabric with ivory scrolling vine embroidery"></div>
  <div class="fabric-photo fabric-photo--rose-damask" role="img" aria-label="Close-up photo of blush fabric with grey damask print"></div>
  <div class="fabric-photo fabric-photo--teal-blossom" role="img" aria-label="Close-up photo of teal satin with white cherry blossom pattern"></div>

  <p class="folio-left">20 | MARLOW CORPORATE CATERING</p>

  <section class="price-panel">
    <h1 class="price-panel__title">TABLE RUNNERS</h1>
    <ul class="price-list">
      <li class="price-list__item"><span>Custom Colours</span><span class="price-list__leader"></span><span>$22.50</span></li>
      <li class="price-list__item"><span>Black + White Flocking</span><span class="price-list__leader"></span><span>$22.50</span></li>
      <li class="price-list__item"><span>Red + White Flocking</span><span class="price-list__leader"></span><span>$22.50</span></li>
      <li class="price-list__item"><span>Chocolate Brown + Black</span><span class="price-list__leader"></span><span>$22.50</span></li>
      <li class="price-list__item"><span>Burgundy + Gold Vine</span><span class="price-list__leader"></span><span>$22.50</span></li>
      <li class="price-list__item"><span>Burgundy + Gold Stripes</span><span class="price-list__leader"></span><span>$22.50</span></li>
      <li class="price-list__item"><span>Floral Leaves</span><span class="price-list__leader"></span><span>$22.50</span></li>
      <li class="price-list__item"><span>Gina</span><span class="price-list__leader"></span><span>$22.50</span></li>
      <li class="price-list__item"><span>Shades of Morocco</span><span class="price-list__leader"></span><span>$22.50</span></li>
      <li class="price-list__item"><span>Ivory + Gold Stripes</span><span class="price-list__leader"></span><span>$22.50</span></li>
      <li class="price-list__item"><span>Ivory + Gold Vine</span><span class="price-list__leader"></span><span>$22.50</span></li>
      <li class="price-list__item"><span>Silver Sequin</span><span class="price-list__leader"></span><span>$22.50</span></li>
      <li class="price-list__item"><span>New York</span><span class="price-list__leader"></span><span>$22.50</span></li>
      <li class="price-list__item"><span>Red + White Check</span><span class="price-list__leader"></span><span>$15.50</span></li>
      <li class="price-list__item"><span>Country Fair</span><span class="price-list__leader"></span><span>$15.50</span></li>
      <li class="price-list__item"><span>Red Pin Tuck Taffeta</span><span class="price-list__leader"></span><span>$15.50</span></li>
      <li class="price-list__item"><span>Blue Cherry Blossom Satin</span><span class="price-list__leader"></span><span>$15.50</span></li>
      <li class="price-list__item"><span>Black Cherry Blossom Satin</span><span class="price-list__leader"></span><span>$15.50</span></li>
      <li class="price-list__item"><span>Fuchsia Hibiscus Satin</span><span class="price-list__leader"></span><span>$15.50</span></li>
    </ul>
  </section>

  <p class="folio-right">21</p>
</div>
</body>
</html>
```